Recently launched Investment banking and Corporate Advisory firm focused and experienced on Selling

We are looking for a dynamic Brochure that can highlight our areas of focus, experience and expertise.
We have a small but seasoned team of professionals in the organisation and want to showcase our ability to provide Growth and / or exit solutions for our clients.
We are a boutique firm and want to focus on showcasing the fact that we strive for excellence and quality and not quantity.

Our core business avtivity at this time is Sell Side M&A services (this means that we sell private businesses). We are unique in our approach to "partnering businesses" with other companies...not just selling them. We focus more on the "strategic fit" of the potential partner rather than the simple valuation that a potential partner (buyer) would place on the company.

We have really been focusing on "GROWTH and EXIT" strategies for private business owners. Customers usually talk to us for 1 of two main reasons. Their businesses are usually very stable or rapidly growing , often to a point where the owners are no longer comfortable running them on their own. They often need capital for expansion or a team to help them expand their business into other countries and markets. for this we look for a solution for them and often it is finding them a strategic partner who will want to buy the majority of the business. There are also the clients that are looking for an exit strategy (typically they are older and getting ready to retire) they are typically seeking for a way to exit the business (sell the business).

A tagline I often use is "Customer Vision" - We see our customers business and needs through their eyes.

Our company website is www.brelvanpartners.com and is a work in progress

Target Market(s)

Business Owners (CEO / Presidents)
Mostly Male
Late 40's to late 60's
Very often they will be Engineers
Very Successful and hard working
Many of them looking for GROWTH solutions
Many of them looking for Retirement
We heavily focus on Oil and Gas Service companies, Oil and Gas manufacturing / oilfield services / Technology Companies and Industrial Companies

Industry/Entity Type

Boutique

Font styles to use
Sans Serif

Colors
f37022
33a6d7

Requirements
Must have
• This must be extremely high quality. The people that will receive these brochures are Presidents and CEO's of companies. Every document we give the customer directly reflects the quality of service we will provide for them.
Nice to have
• Pictures tell a great story and can also tell about the areas of experience and expertise that we have

Ideally we'd be interested in a square shaped marketing document (signifies strength and solidness in the business/opportunity) - either 5x5 or 7x7 size in a 4-6 page (double-sided) saddle-stitched booklet.
We'd like to relay an emotion while also describing our business.

```html
<!DOCTYPE html>
<html lang="en">
<head>
<meta charset="utf-8">
<title>Merger and Acquisition Advisory Services — Brelvan Partners</title>
<link rel="stylesheet" href="https://fonts.googleapis.com/css2?family=Baumans&family=Didact+Gothic&family=Questrial&display=swap">
<style>
  :root {
    --brand-blue: #1a7bc4;
    --text-blue: #1b78c2;
    --tab-text: #2b8fdc;
    --brand-orange: #f26a22;
    --page-light: #fbfbfb;
    --page-edge: #dcdcdc;
    --tab-gap: #cfe3f2;
  }
  * { box-sizing: border-box; margin: 0; padding: 0; }
  html, body { width: 1200px; height: 1200px; overflow: hidden; }
  body { background: #ffffff; }

  .page {
    position: relative;
    width: 1200px;
    height: 1200px;
    overflow: hidden;
    font-family: "Didact Gothic", "Questrial", sans-serif;
    color: var(--text-blue);
  }

  .page-body {
    position: absolute;
    left: 0; top: 0;
    width: 1008px; height: 1078px;
    background: radial-gradient(ellipse at 45% 40%, var(--page-light) 0%, #f1f1f1 55%, var(--page-edge) 100%);
  }

  .footer-band {
    position: absolute;
    left: 0; top: 1078px;
    width: 1008px; height: 122px;
    background: var(--brand-blue);
  }

  .page-title {
    position: absolute;
    left: 0; top: 118px;
    width: 1032px;
    text-align: center;
    font-family: "Questrial", sans-serif;
    font-weight: 400;
    font-size: 44px;
    letter-spacing: 0.3px;
    color: var(--brand-blue);
  }

  .section-title {
    position: absolute;
    left: 0; top: 291px;
    width: 1012px;
    text-align: center;
    font-family: "Questrial", sans-serif;
    font-size: 26px;
    color: var(--brand-blue);
  }

  .column-divider {
    position: absolute;
    left: 498px; top: 354px;
    width: 3px; height: 668px;
    background: var(--brand-blue);
  }

  .service-column {
    position: absolute;
    font-size: 20.5px;
    line-height: 25.6px;
  }
  .service-column.buy-side { left: 62px; top: 421px; }
  .service-column.sell-side { left: 550px; top: 415px; }

  .side-label { margin-bottom: 26px; }
  .side-intro { margin-bottom: 86px; }
  .service-list { list-style: none; padding-left: 29px; }
  .service-list li::before { content: "*"; }
  .service-list .wrap { padding-left: 12px; display: block; }

  .section-nav {
    position: absolute;
    left: 982px; top: 0;
    width: 218px; height: 1200px;
    background: var(--tab-gap);
  }
  .nav-tab {
    position: absolute;
    left: 26px;
    width: 192px;
    height: 128px;
    background: var(--brand-orange);
    font-family: "Baumans", sans-serif;
    font-size: 28px;
    line-height: 40px;
    text-align: right;
    padding-right: 10px;
    color: var(--tab-text);
    display: flex;
    flex-direction: column;
    justify-content: center;
    align-items: flex-end;
  }
  .nav-tab.compact { font-size: 25px; }
  .nav-tab.active {
    left: 0; top: 0;
    width: 218px; height: 136px;
    background: transparent;
    color: #ffffff;
    align-items: center;
    padding: 0 0 0 26px;
  }
  .nav-tab.active svg { position: absolute; left: 0; top: 0; }
  .nav-tab.active span { position: relative; text-align: left; }
</style>
</head>
<body>
<main class="page">
  <div class="page-body"></div>
  <div class="footer-band"></div>

  <h1 class="page-title">Merger and Acquisition Advisory Services</h1>
  <h2 class="section-title">Merger &amp; Acquisition Advisory</h2>
  <div class="column-divider"></div>

  <section class="service-column buy-side">
    <p class="side-label">-Buy Side-</p>
    <p class="side-intro">If you want to expand your business in<br>a specific geographic area or industry<br>we will help you target potential<br>acquisitions, negotiate a deal and<br>complete your diligence.</p>
    <p>Our services include:</p>
    <ul class="service-list">
      <li>Synergy business plans</li>
      <li>Recast financial</li>
      <li>Brief writing and generation</li>
      <li>Extensive research</li>
      <li>Business intelligence reports</li>
      <li>Market studies/reports</li>
      <li>Feasibility studies</li>
      <li>Coaching and mentoring</li>
      <li>Contract negotiations</li>
      <li>Due diligence facilitation</li>
      <li>Project management</li>
    </ul>
  </section>

  <section class="service-column sell-side">
    <p class="side-label">-Sell Side-</p>
    <p class="side-intro">After a health check on the viability of<br>going to market, Brelvan Partners<br>will use proven systems to<br>assist you in taking your business to<br>market and maximizing the value of<br>your company.</p>
    <p style="margin-top:-26px">We provide:</p>
    <ul class="service-list">
      <li>Synergy business plans</li>
      <li>Recast financial</li>
      <li>Financial business plans</li>
      <li>Extensive research</li>
      <li>Prospectus/Information memorandum<span class="wrap">writing and generation</span></li>
      <li>Detailed research lists</li>
      <li>Coaching and mentoring</li>
      <li>Contract negotiations</li>
      <li>Due diligence facilitation</li>
      <li>Outbound prospect generation</li>
      <li>Project management</li>
    </ul>
  </section>

  <nav class="section-nav">
    <div class="nav-tab active">
      <svg width="218" height="136" viewBox="0 0 218 136" aria-hidden="true">
        <polygon points="32,0 218,0 218,136 32,136 0,68" fill="var(--brand-blue)"/>
      </svg>
      <span>Mergers &amp;<br>Acquisitions</span>
    </div>
    <div class="nav-tab" style="top:138px">Risk<br>Management</div>
    <div class="nav-tab" style="top:272px">Business<br>Development<br>Solution</div>
    <div class="nav-tab" style="top:406px">Growth<br>Solution</div>
    <div class="nav-tab" style="top:540px">Exit<br>Strategies</div>
    <div class="nav-tab" style="top:674px">Sales &amp;<br>Marketing<br>Solution</div>
    <div class="nav-tab compact" style="top:808px">Communications<br>Solution</div>
    <div class="nav-tab" style="top:942px">Outsourced<br>Solution</div>
    <div class="nav-tab" style="top:1076px;height:124px">Special<br>Projects<br>Solution</div>
  </nav>
</main>
</body>
</html>
```